Wine bottle label for family vineyard

Label front and back for our background vineyard. BeLow is a label we used in the past. The gazebo is at the top of the vineyard. We want the front label to have the info we have currently with name etc. But we are open to fun on the back. Maybe a Covid mask would be appropriate Would like one with and one without. But I want the designer to feel free and go out of the box. Especially on back label.

Target Market(s)

None. It’s just for personal consumption We drink what we can and give the rest away.

Industry/Entity Type

Wine

Requirements
Must have
• Name the quiet glass. Tosbeck family vineyard. Pinot noir. Year. Name of winemaker.
Nice to have
• The back label being fun is a plus. Maybe some quotes about wine and friends

```html
<!DOCTYPE html>
<html lang="en">
<head>
<meta charset="utf-8">
<title>The Quiet Glass – Wine Labels</title>
<link rel="stylesheet" href="https://fonts.googleapis.com/css2?family=Gochi+Hand&family=Kaushan+Script&family=Oswald:wght@600;700&display=swap">
<style>
  :root {
    --label-red: #a10a0a;
    --label-gold: #d9a15a;
    --ink-white: #ffffff;
    --ink-black: #111111;
    --brand-red: #c8100f;
    --band-dark: #232e2b;
    --photo-light: #e6e6e6;
    --photo-mid: #9a9a9a;
    --photo-dark: #2a2a2a;
    --emblem-yellow: #f6b21c;
    --emblem-orange: #e27a12;
    --emblem-shadow: #5a0606;
  }
  html, body {
    margin: 0;
    padding: 0;
    width: 1200px;
    height: 1110px;
    overflow: hidden;
    background: #ffffff;
  }
  .labels { display: block; width: 1200px; height: 1110px; }
  .label-frame { stroke: var(--label-gold); stroke-width: 10; }
  .back-label .label-frame { fill: var(--label-red); }
  .front-label .label-frame { fill: var(--photo-light); }
  .front-label .frame-outline { fill: none; }
  .script-line {
    font-family: "Kaushan Script", cursive;
    fill: var(--ink-white);
    text-anchor: middle;
  }
  .brand-name {
    font-family: "Gochi Hand", cursive;
    text-anchor: middle;
  }
  .back-label .brand-name { fill: var(--ink-white); }
  .front-label .brand-name { fill: var(--brand-red); }
  .brand-sub {
    font-family: "Gochi Hand", cursive;
    text-anchor: middle;
  }
  .back-label .brand-sub { fill: var(--ink-white); }
  .front-label .brand-sub { fill: var(--ink-black); }
  .house-mark { font-family: "Gochi Hand", cursive; fill: var(--brand-red); text-anchor: middle; }
  .house-dot { fill: var(--brand-red); }
  .varietal {
    font-family: "Oswald", sans-serif;
    font-weight: 700;
    fill: var(--ink-white);
    text-anchor: middle;
  }
  .appellation {
    font-family: "Oswald", sans-serif;
    font-weight: 600;
    fill: var(--ink-white);
    text-anchor: middle;
  }
  .band { fill: var(--band-dark); }
</style>
</head>
<body>
<svg class="labels" viewBox="0 0 1200 1110" xmlns="http://www.w3.org/2000/svg">
  <defs>
    <path id="label-shape" d="M32 85 Q288 -25 545 85 A45 45 0 0 0 577 130 L577 970 A45 45 0 0 0 545 1015 Q288 1125 32 1015 A45 45 0 0 0 0 970 L0 130 A45 45 0 0 0 32 85 Z"/>
    <clipPath id="front-clip"><use href="#label-shape"/></clipPath>
    <linearGradient id="garden-photo" x1="0" y1="0" x2="0" y2="1">
      <stop offset="0" stop-color="var(--photo-dark)"/>
      <stop offset="0.35" stop-color="var(--photo-mid)"/>
      <stop offset="0.7" stop-color="var(--photo-light)"/>
      <stop offset="1" stop-color="var(--photo-mid)"/>
    </linearGradient>
    <radialGradient id="survivor-emblem" cx="0.5" cy="0.48" r="0.5">
      <stop offset="0" stop-color="var(--emblem-yellow)"/>
      <stop offset="0.45" stop-color="var(--emblem-orange)" stop-opacity="0.9"/>
      <stop offset="0.8" stop-color="var(--emblem-shadow)" stop-opacity="0.35"/>
      <stop offset="1" stop-color="var(--label-red)" stop-opacity="0"/>
    </radialGradient>
  </defs>

  <!-- Back label -->
  <g class="back-label" transform="translate(2,4)">
    <use href="#label-shape" class="label-frame"/>
    <text class="script-line" x="276" y="133" font-size="46">This vintage of</text>
    <text class="brand-name" x="280" y="238" font-size="62">The Quiet Glass</text>
    <text class="brand-sub" x="280" y="282" font-size="33">A Tosbeck Family Vineyard</text>
    <text class="script-line" x="298" y="392" font-size="54">is dedicated to:</text>
    <ellipse cx="262" cy="780" rx="250" ry="262" fill="url(#survivor-emblem)" role="img" aria-label="Cartoon emblem giving a thumbs up while wearing a face mask, above a red ribbon reading Survivor"/>
  </g>

  <!-- Front label -->
  <g class="front-label" transform="translate(620,6)">
    <use href="#label-shape" class="label-frame"/>
    <g clip-path="url(#front-clip)">
      <rect x="0" y="0" width="577" height="900" fill="url(#garden-photo)" role="img" aria-label="Black and white photograph of the garden gazebo at the top of the vineyard"/>
      <path class="band" d="M0 792 Q288 976 577 792 L577 1110 L0 1110 Z"/>
    </g>
    <use href="#label-shape" class="label-frame frame-outline"/>
    <text class="brand-name" x="292" y="566" font-size="74">The Quiet Glass</text>
    <text class="brand-sub" x="296" y="624" font-size="40">A Tosbeck Family Vineyard</text>
    <circle class="house-dot" cx="204" cy="738" r="10"/>
    <text class="house-mark" x="304" y="752" font-size="46">Tosbeck</text>
    <text class="varietal" x="294" y="936" font-size="42">PINOT NOIR</text>
    <text class="appellation" x="290" y="980" font-size="26">Sonoma Border</text>
    <text class="appellation" x="290" y="1010" font-size="26" xml:space="preserve">Novato  Marin County 2016</text>
  </g>
</svg>
</body>
</html>
```